Bus. Card/Envelope/Letterhead Design Request with my Logo

I have a logo created. I need to create a business card design, letterhead design and envelope design with the new logo.
Updates

The logo has now been posted. Thank you.

Target Market(s)

Professional. Legal Field.

Industry/Entity Type

Business

Requirements
Must have
• I like the same font as the logo.

```html
<!DOCTYPE html>
<html lang="en">
<head>
<meta charset="utf-8">
<title>Carrow Linden LLP – Business Card</title>
<link href="https://fonts.googleapis.com/css2?family=Cinzel:wght@400;500&family=Lato:wght@400&family=Arimo&display=swap" rel="stylesheet">
<style>
  :root {
    --green: #77e000;
    --white: #ffffff;
    --ink: #111111;
    --grey: #8a8a8a;
    --frame: #9a9a9a;
    --card-edge: #e2e2e2;
  }
  * { margin: 0; padding: 0; box-sizing: border-box; }
  html, body { width: 1200px; height: 494px; overflow: hidden; background: var(--white); }
  .sheet { position: relative; width: 1200px; height: 494px; }
  .frame { position: absolute; left: 0; top: 0; width: 1199px; height: 414px; border: 1px solid var(--frame); }

  .card { position: absolute; top: 50px; height: 326px; }
  .card--front { left: 55px; width: 534px; background: var(--green); }
  .card--back { left: 589px; width: 534px; background: var(--white); border: 1px solid var(--card-edge); border-left: none; }

  /* front */
  .front-mark { position: absolute; left: 56px; top: 142px; width: 120px; height: 120px; border-radius: 50%; background: var(--white); }
  .front-name { position: absolute; left: 196px; top: 180px; font-family: "Cinzel", serif; font-size: 30px; color: var(--white); letter-spacing: 1px; }
  .front-tagline { position: absolute; left: 116px; top: 282px; width: 380px; display: flex; align-items: center; gap: 22px;
    font-family: "Lato", sans-serif; font-size: 13px; letter-spacing: 5.5px; color: var(--white); white-space: nowrap; }
  .front-tagline .rule { flex: 1; height: 1px; background: var(--white); }

  /* back */
  .brand { position: absolute; left: 38px; top: 16px; width: 266px; text-align: center; }
  .brand-dot { width: 34px; height: 34px; border-radius: 50%; background: var(--green); margin: 0 auto -6px; position: relative; z-index: 1; }
  .brand-rule { height: 2px; background: var(--ink); }
  .brand-name { font-family: "Cinzel", serif; font-size: 21px; color: var(--ink); letter-spacing: 1px; padding: 6px 0 4px; white-space: nowrap; }
  .brand-tagline { display: flex; align-items: center; justify-content: center; gap: 12px; margin-top: 6px;
    font-family: "Cinzel", serif; font-size: 8.5px; letter-spacing: 3px; color: var(--ink); }
  .brand-tagline .rule { width: 28px; height: 1px; background: var(--ink); }

  .person { position: absolute; left: 110px; top: 124px; font-family: "Lato", sans-serif; }
  .person-name { font-size: 30px; color: var(--green); line-height: 1; }
  .person-title { font-size: 21px; color: var(--ink); margin-top: 10px; line-height: 1; }
  .contact { list-style: none; margin-top: 6px; font-size: 15px; color: var(--grey); line-height: 20.5px; }
  .address { position: absolute; left: 83px; top: 288px; font-family: "Lato", sans-serif; font-size: 15px; color: var(--grey); }

  .label { position: absolute; top: 437px; font-family: "Arimo", sans-serif; font-size: 46px; color: var(--ink); }
  .label--front { left: 134px; }
  .label--back { left: 704px; }
</style>
</head>
<body>
<main class="sheet">
  <div class="frame"></div>

  <section class="card card--front" aria-label="Front of card">
    <div class="front-mark"></div>
    <div class="front-name">Carrow Linden</div>
    <div class="front-tagline"><span class="rule"></span>ATTORNEYS AT LAW<span class="rule"></span></div>
  </section>

  <section class="card card--back" aria-label="Back of card">
    <div class="brand">
      <div class="brand-dot"></div>
      <div class="brand-rule"></div>
      <div class="brand-name">Carrow Linden LLP</div>
      <div class="brand-rule"></div>
      <div class="brand-tagline"><span class="rule"></span>ATTORNEYS AT LAW<span class="rule"></span></div>
    </div>

    <div class="person">
      <div class="person-name">NAME</div>
      <div class="person-title">DESIGNATION</div>
      <ul class="contact">
        <li>oxoxoxoxoxoxoxo : Phone</li>
        <li>xoxoxoxoxoxoxox :</li>
        <li>abcdefgh@carrowlinden.com</li>
        <li>www.examplesiteaddress.com</li>
      </ul>
    </div>
    <p class="address">This the space for address, not the actual content</p>
  </section>

  <p class="label label--front">Front card</p>
  <p class="label label--back">Back card</p>
</main>
</body>
</html>
```